Need simple and modern looking business card with all my information on one side and logo on the other side
Info :
Company name - VELMAR CONSTRUCTION LLC
Company addres- 418 harbor 87th. Dunmoor park ny 10352
Email- velmarllc@tridomail.Com
Company phone number 555-318-6094
Cell number- 555-742-0583
Web site - velmarllc.Com
My name Gerald tomasino

Target Market(s)

Construction , home improvement, remodeling

Industry/Entity Type

Construction

Contact Information for Business Card

It has to be moder but at the same time simple

Font styles to use
Sans Serif

Colors
0255a3
ffffff
000000
f78f20
b1b1b1
9d9d9d
1b1b1b
33a6d7
ec1f27

Requirements
Must have
• My logo on one side maybe with a some kind of background on the other side all my information
Nice to have
• Some kind of background pictures provided by you .PLEASE HAVE ACCOUNT WITH PIXELVAULT WILL NOT PAY ANY EXTRA FEES .
Should not have
• Any kind of hamer, nails,screws, helmets itp. Please do not copy the other designs come up with something new.

```html
<!DOCTYPE html>
<html lang="en">
<head>
<meta charset="utf-8">
<title>Velmar Construction LLC – Business Card</title>
<link rel="stylesheet" href="https://fonts.googleapis.com/css2?family=Source+Sans+3:wght@400;600;700&display=swap">
<style>
  :root {
    --stage: #1e1e1e;
    --card-white: #ffffff;
    --card-grey: #c4c7cb;
    --card-grey-light: #e9eaec;
    --band-green: #b1cf3a;
    --name-blue: #0255a3;
    --title-red: #ec1f27;
    --ink: #000000;
    --mark-orange: #f78f20;
    --mark-grey: #9d9d9d;
  }
  * { box-sizing: border-box; margin: 0; padding: 0; }
  html, body {
    width: 1200px; height: 1200px; overflow: hidden;
    background: var(--stage);
    font-family: "Source Sans 3", "Helvetica Neue", Arial, sans-serif;
  }
  .card {
    position: absolute; left: 175px;
    width: 850px; height: 486px;
    overflow: hidden;
    box-shadow: 0 8px 24px rgba(0,0,0,.5);
  }
  .card--front { top: 90px; }
  .card--back  { top: 624px; }

  .card__photo { position: absolute; inset: 0; }
  .card--front .card__photo {
    background: radial-gradient(ellipse 55% 50% at 58% 48%, var(--card-white) 0%, var(--card-grey-light) 45%, var(--card-grey) 100%);
  }
  .card--back .card__photo {
    background:
      linear-gradient(180deg, var(--card-grey-light) 0%, var(--card-white) 32%, var(--card-white) 62%, var(--card-grey-light) 100%);
  }

  .card__band {
    position: absolute; top: 0; bottom: 0;
    width: 215px; background: var(--band-green);
  }
  .card--front .card__band { left: 42px; }
  .card--back .card__band { left: 0; }

  .brand-box {
    position: absolute; left: 42px; top: 52px;
    width: 220px; height: 140px;
    background: var(--card-white);
    display: flex; align-items: center; justify-content: center;
  }

  .brand {
    display: flex; align-items: center; gap: 10px;
    color: var(--ink); font-weight: 600;
  }
  .brand__square { width: 26px; height: 26px; background: var(--mark-orange); flex: none; }
  .brand__text { line-height: 1; }
  .brand__name { display: block; font-size: 34px; letter-spacing: 1px; }
  .brand__sub { display: block; font-size: 12.5px; letter-spacing: 1px; margin-top: 4px; }

  .holder-name {
    position: absolute; top: 54px; right: 42px;
    color: var(--name-blue); font-weight: 700; font-size: 31px;
  }
  .company-title {
    position: absolute; top: 206px; left: 300px;
    color: var(--title-red); font-weight: 700; font-size: 45px;
    letter-spacing: -0.5px; line-height: 1.05;
    border-bottom: 2px solid var(--title-red);
    padding-bottom: 2px;
  }
  .contact {
    position: absolute; left: 440px; top: 334px;
    list-style: none; color: var(--ink);
    font-weight: 700; font-size: 19px; line-height: 1.22;
  }

  .card--back .brand { position: absolute; right: 70px; bottom: 120px; }
  .card--back .brand__name { font-size: 44px; }
  .card--back .brand__sub { font-size: 16px; }
  .card--back .brand__square { width: 32px; height: 32px; }
</style>
</head>
<body>
  <section class="card card--front">
    <div class="card__photo" role="img" aria-label="Soft grey photograph of a modern glass office building facade"></div>
    <div class="card__band"></div>
    <div class="brand-box">
      <div class="brand">
        <span class="brand__square"></span>
        <span class="brand__text">
          <span class="brand__name">VELMAR</span>
          <span class="brand__sub">CONSTRUCTION LLC</span>
        </span>
      </div>
    </div>
    <p class="holder-name">Gerald tomasino</p>
    <h1 class="company-title">VELMAR CONSTRUCTION LLC</h1>
    <ul class="contact">
      <li>418 harbor 87th. Dunmoor park ny 10352</li>
      <li>Email- velmarllc@tridomail.Com</li>
      <li>Company phone number 555-318-6094</li>
      <li>Cell number- 555-742-0583</li>
      <li>Web site - velmarllc.Com</li>
    </ul>
  </section>

  <section class="card card--back">
    <div class="card__photo" role="img" aria-label="Faint light photograph of a modern building facade fading to white"></div>
    <div class="card__band"></div>
    <div class="brand">
      <span class="brand__square"></span>
      <span class="brand__text">
        <span class="brand__name">VELMAR</span>
        <span class="brand__sub">CONSTRUCTION LLC</span>
      </span>
    </div>
  </section>
</body>
</html>
```